delivery service for warm food for kids and other kids stuff

plumborre.nl > daycare website

plumborre.shop >>> shopify site we ask you to design!

We are a daycare center and thanks to corona found that we could help parents and kids while at home ! we would like some help to get an awesome and clear site for this.

it doesnt have to look kiddy...
more proffessional and sleek
we love quindle website... so anything in that direction would be great!... ie pic next to text...
2 tone colors
ours are pink light blue and white.. so play with that?
black and white also fine!

Target Market(s)

expats and proffesional parents ... so NOT KIDDY website...

Font styles to use
Sans Serif

Requirements
Must have
• sexy design....
simplicity...
less text... more pictures
cool headlines
Should not have
• lots of text everyhwere
busy

```html
<!DOCTYPE html>
<html lang="en">
<head>
<meta charset="utf-8">
<title>Plumborre Shop</title>
<link rel="stylesheet" href="https://fonts.googleapis.com/css2?family=Arimo:wght@400;700&display=swap">
<style>
:root{
  --pink:#d9376e;
  --blue:#1f9dd6;
  --cyan:#1cc0e8;
  --ink:#1d1d1f;
  --grey:#5c5c63;
  --muted:#8a8a90;
  --line:#e3e3e6;
  --white:#ffffff;
}
*{margin:0;padding:0;box-sizing:border-box}
html,body{width:1200px;height:4270px;overflow:hidden;background:var(--white)}
body{font-family:"Arimo",Arial,sans-serif;color:var(--ink);position:relative}
.abs{position:absolute}
.center{text-align:center}
.photo{position:absolute;display:block}

/* header */
.brand{left:55px;top:6px;width:106px;height:106px;border:3px solid var(--blue);border-radius:50%;display:flex;align-items:center;justify-content:center}
.brand-name{font-size:15px;font-weight:700;color:var(--pink);text-align:center;line-height:1.15}
.nav a{position:absolute;top:47px;font-size:13px;color:#333;text-decoration:none;letter-spacing:.3px}
.nav a.active{color:var(--pink)}

/* buttons */
.btn{position:absolute;display:flex;align-items:center;justify-content:center;font-weight:700;text-decoration:none;letter-spacing:.5px}
.btn-pink{background:var(--pink);color:var(--white)}
.btn-blue{background:var(--blue);color:var(--white)}
.btn-white{background:var(--white);color:var(--pink)}

.section-title{position:absolute;left:0;width:1200px;text-align:center}

/* hero card */
.hero-card{left:744px;top:456px;width:338px;height:169px;background:var(--white)}
.hero-card .t1{position:absolute;top:28px;width:100%;text-align:center;font-size:27px;font-weight:700;color:var(--blue)}
.hero-card .t2{position:absolute;top:61px;width:100%;text-align:center;font-size:25px;color:var(--pink)}

.overlay-label{left:451px;top:960px;width:320px;text-align:center;color:var(--white)}
.overlay-label .name{font-size:20px;letter-spacing:.5px}
.overlay-label .link{font-size:15px;text-decoration:underline;margin-top:4px}

.daycare-box{left:326px;top:1460px;width:517px;height:209px;background:var(--blue);color:var(--white);text-align:center}
.daycare-box h2{position:absolute;top:38px;width:100%;font-size:26px;font-weight:400}
.daycare-box p{position:absolute;top:80px;left:40px;right:40px;font-size:11.5px;line-height:17px}

.why-title{left:136px;top:2012px;font-size:37px;line-height:46px;color:var(--pink);font-weight:400}
.why-copy{left:139px;top:2170px;width:390px;font-size:19px;line-height:28.5px;color:var(--grey)}
.why-link{left:139px;top:2312px;font-size:17px;font-weight:700;color:var(--blue);text-decoration:underline}

.quality{position:absolute;top:2764px;width:220px;text-align:center}
.quality svg{display:block;margin:0 auto}
.quality .label{margin-top:40px;font-size:16px;line-height:22px;color:var(--ink)}

.nursery{left:113px;top:3016px;width:976px;height:479px}
.nursery-text{left:113px;width:976px;text-align:center;color:var(--white)}

.blog-caption{position:absolute;top:3848px;width:305px;font-size:15.5px;line-height:20px;color:var(--ink)}
.blog-date{position:absolute;top:3904px;font-size:12.5px;color:var(--muted)}

.footer-text{font-size:13.5px;color:#333}
.social{position:absolute;top:4152px;width:18px;height:18px;border-radius:50%;background:var(--blue)}
.email{left:824px;top:4080px;width:253px;height:44px;border:1px solid var(--line);font-size:12px;color:var(--muted);padding:15px 18px}
.card-badge{position:absolute;top:4176px;width:36px;height:22px;border-radius:3px}
</style>
</head>
<body>

<!-- header -->
<div class="abs brand"><span class="brand-name">PLUMBORRE<br>SHOP</span></div>
<nav class="nav">
  <a class="active" href="#" style="left:244px">HOME</a>
  <a href="#" style="left:317px">ABOUT US</a>
  <a href="#" style="left:419px">POLICY</a>
  <a href="#" style="left:502px">DAY CARE</a>
  <a href="#" style="left:602px">REGISTER</a>
  <a href="#" style="left:704px">CONTACT</a>
  <a href="#" style="left:951px">SEARCH</a>
  <a href="#" style="left:1036px">FOLLOW</a>
  <a href="#" style="left:1119px">CART</a>
</nav>

<!-- hero -->
<div class="photo" role="img" aria-label="Toddlers playing with modelling clay at a blue classroom table" style="left:0;top:114px;width:600px;height:577px;background:linear-gradient(160deg,#b9d98f 0%,#e8d9c4 45%,#3f6fc9 100%)"></div>
<div class="photo" role="img" aria-label="Lunch box with rice, egg and vegetables beside fresh fruit and tomatoes" style="left:600px;top:114px;width:600px;height:577px;background:linear-gradient(200deg,#9bc96a 0%,#f1f1ee 40%,#e9e6e2 70%,#e8503a 100%)"></div>
<div class="abs hero-card">
  <div class="t1">CURATED FOR YOU</div>
  <div class="t2">PLUMBORRE KIDS!</div>
  <a class="btn btn-pink" href="#" style="left:106px;top:104px;width:126px;height:41px;font-size:11.5px">LEARN MORE</a>
</div>

<!-- featured collection -->
<h2 class="section-title" style="top:748px;font-size:27px;font-weight:400;color:var(--pink)">FEATURED COLLECTION</h2>
<div class="photo" role="img" aria-label="Bottles of fresh fruit and vegetable juice with straws" style="left:119px;top:823px;width:302px;height:342px;background:linear-gradient(180deg,#eef0ec 0%,#d4574f 70%,#c9d7c2 100%)"></div>
<div class="photo" role="img" aria-label="Bowl of pasta bolognese on a lawn" style="left:451px;top:823px;width:301px;height:342px;background:linear-gradient(180deg,#4c5d3d 0%,#8d8f86 50%,#b33a25 100%)"></div>
<div class="abs overlay-label"><div class="name">PASTA BOLOGNESE</div><div class="link">SHOP NOW</div></div>
<div class="photo" role="img" aria-label="Plated risotto with tomato garnish on grass" style="left:780px;top:823px;width:302px;height:342px;background:radial-gradient(circle at 50% 55%,#e7e39a 0%,#7c8a5f 45%,#3e5c2a 100%)"></div>
<a class="btn btn-blue" href="#" style="left:494px;top:1200px;width:214px;height:40px;font-size:13px">VIEW ALL COLLECTION</a>

<!-- day care band -->
<div class="photo" role="img" aria-label="Children eating lunch together at a table with fruit" style="left:106px;top:1309px;width:976px;height:505px;background:linear-gradient(180deg,#c9a56d 0%,#e7d8bf 50%,#c6b48d 100%)"></div>
<div class="abs daycare-box">
  <h2>DAY CARE SERVICES</h2>
  <p>Augiat in pede Fusce tellus Sed metus augue convallis et vehicula ut pulvinar eu ante Integer orci tellus tristique vitae</p>
  <a class="btn btn-white" href="#" style="left:156px;top:134px;width:214px;height:40px;font-size:13px">UPLOAD PRESCRIPTION</a>
</div>

<!-- why section -->
<h2 class="abs why-title">WHY PLUMBORRE<br>DAYCARE IS THE<br>BEST CHOICE</h2>
<p class="abs why-copy">Augiat in pede Fusce tellus Sed metus augue convallis et vehicula ut pulvinar eu ante Integer orci tellus tristique vitae consequat nec mauris viverra in</p>
<a class="abs why-link" href="#">LEARN MORE</a>
<div class="photo" role="img" aria-label="Teacher helping a girl build with wooden blocks" style="left:641px;top:1940px;width:441px;height:511px;background:linear-gradient(170deg,#e9e4dc 0%,#d6c5ad 55%,#b98b5e 100%)"></div>

<!-- qualities -->
<h2 class="section-title" style="top:2590px;font-size:34px;font-weight:400;color:var(--blue)">OUR QUALITIES</h2>
<p class="section-title" style="top:2648px;font-size:19px;color:var(--grey)">We love what we do &amp; we do it with passion!</p>

<div class="quality" style="left:124px">
  <svg width="86" height="66" viewBox="0 0 86 66" fill="none" stroke="var(--pink)" stroke-width="2.5" stroke-linecap="round">
    <path d="M38 18 A18 18 0 1 0 40 46"/><path d="M48 48 A18 18 0 1 0 46 20"/>
    <path d="M32 12 l7 6 -7 6"/><path d="M54 54 l-7 -6 7 -6"/>
  </svg>
  <div class="label">UNMATCHED<br>FLEXIBILITY</div>
</div>
<div class="quality" style="left:384px">
  <svg width="86" height="66" viewBox="0 0 86 66" fill="none" stroke="var(--pink)" stroke-width="2.5">
    <ellipse cx="32" cy="26" rx="20" ry="18"/><path d="M20 40 l-6 10 14-6"/>
    <ellipse cx="56" cy="38" rx="18" ry="16" fill="var(--white)"/>
    <path d="M50 46 l6-16 6 16 M52 41 h8" stroke-width="2.2"/>
    <path d="M24 20 h16 M32 16 v4 M26 32 l12-10 M28 24 l10 8" stroke-width="2.2"/>
  </svg>
  <div class="label">BILINGUAL<br>GUIDANCE</div>
</div>
<div class="quality" style="left:606px">
  <svg width="86" height="66" viewBox="0 0 86 66" fill="none" stroke="var(--pink)" stroke-width="2.5">
    <circle cx="43" cy="33" r="29"/><ellipse cx="43" cy="33" rx="12" ry="29"/>
    <path d="M14 33 h58 M19 18 h48 M19 48 h48"/>
  </svg>
  <div class="label">33+<br>CULTURES</div>
</div>
<div class="quality" style="left:858px">
  <svg width="86" height="66" viewBox="0 0 86 66" fill="none" stroke="var(--pink)" stroke-width="2.5" stroke-linecap="round">
    <path d="M43 18 C30 8 14 16 16 34 C18 52 32 64 43 58 C54 64 68 52 70 34 C72 16 56 8 43 18 Z"/>
    <path d="M43 18 C43 10 46 5 50 2"/><path d="M47 12 C54 4 62 6 64 8 C58 14 52 14 47 12 Z"/>
  </svg>
  <div class="label">ORGANIC<br>VERY LOGICAL</div>
</div>

<!-- nursery band -->
<div class="photo nursery" role="img" aria-label="Two laughing children playing on the floor, tinted blue" style="background:linear-gradient(135deg,#2cc8ef 0%,#18b6e2 50%,#2ab0db 100%)"></div>
<h2 class="abs nursery-text" style="top:3140px;font-size:36px;font-weight:400;line-height:43px">YOUR NURSERY<br>FOR 15 YEARS</h2>
<p class="abs nursery-text" style="top:3240px;font-size:12.5px;line-height:19px">Over the past few years, we have raised thousands of children in the Leiden region<br>with passion and dedication and it is our goal to help both new</p>
<a class="btn btn-pink" href="#" style="left:489px;top:3294px;width:194px;height:48px;font-size:17px;font-weight:400">LEARN MORE</a>

<!-- blogs -->
<h2 class="section-title" style="top:3552px;font-size:28px;font-weight:400;color:var(--ink)">RECENT BLOGS</h2>
<div class="photo" role="img" aria-label="Girl on a colourful playground swing" style="left:113px;top:3621px;width:305px;height:210px;background:linear-gradient(180deg,#c73b34 0%,#e7c99b 50%,#3a63b6 100%)"></div>
<div class="photo" role="img" aria-label="Two girls eating a snack together" style="left:449px;top:3621px;width:303px;height:210px;background:linear-gradient(180deg,#f3efea 0%,#d8b18d 55%,#5673a9 100%)"></div>
<div class="photo" role="img" aria-label="Children and a teacher playing with toys in a classroom" style="left:785px;top:3621px;width:304px;height:210px;background:linear-gradient(180deg,#e7ddd3 0%,#d6a6a2 55%,#d85a42 100%)"></div>
<p class="blog-caption" style="left:113px">Augiat in pede Fusce tellus Sed metus augue convallis et vehicula</p>
<p class="blog-caption" style="left:454px">Augiat in pede Fusce tellus Sed metus augue convallis et vehicula</p>
<p class="blog-caption" style="left:785px">Augiat in pede Fusce tellus Sed metus augue convallis et vehicula</p>
<span class="blog-date" style="left:113px">APR 15 2020</span>
<span class="blog-date" style="left:454px">APR 15 2020</span>
<span class="blog-date" style="left:785px">APR 15 2020</span>
<a class="btn btn-pink" href="#" style="left:522px;top:3955px;width:151px;height:47px;font-size:15px">VIEW ALL</a>

<!-- footer -->
<p class="abs footer-text" style="left:106px;top:4082px">© 2020 Company Name I All Rights Reserved</p>
<p class="abs footer-text" style="left:106px;top:4115px">Term of Use I Privacy Policy</p>
<span class="social" style="left:102px"></span>
<span class="social" style="left:152px"></span>
<span class="social" style="left:201px"></span>
<span class="social" style="left:251px"></span>
<p class="abs footer-text" style="left:565px;top:4082px">About</p>
<p class="abs footer-text" style="left:565px;top:4115px">Day Care</p>
<p class="abs footer-text" style="left:565px;top:4148px">Contact Us</p>
<div class="abs email">Your Email</div>
<a class="btn btn-pink" href="#" style="left:1087px;top:4080px;width:55px;height:44px;font-size:14px;font-weight:400">OK</a>
<span class="card-badge" style="left:820px;background:#e9ecf3"></span>
<span class="card-badge" style="left:877px;background:#f1e6de"></span>
<span class="card-badge" style="left:933px;background:#2f6fc4"></span>
<span class="card-badge" style="left:989px;background:#e8eef7"></span>
<span class="card-badge" style="left:1045px;background:#e6edf5"></span>
<span class="card-badge" style="left:1101px;background:#f4ebe2"></span>

</body>
</html>
```